Verdant Shield - All Natural Insecticide for Agriculture Market - eliminating chemicals in our food

Our company is Fieldstone Harvest Works (FHW). We supply natural fertilizers and insecticide to the agriculture market. We need a design for a product that we call Verdant Shield. This is a product that a farmer or a home owner could use as a barrier to troublesome insects. It is 100% natural and keeps bugs away much longer than the conventional chemicals out there, and ours is safe. The initial thought was some kind of a see through dome which you could see maybe some corn stalks through the dome, maybe some livestock, maybe a house...and some insects trying to penetrate the dome and not being able to. The agriculture market is our main market so it needs to include corn or some kind of row crop probably in the graphic.

This is the first of many graphics that we will need. We currently have about 8 products...and growing.

Target Market(s)

Farmers for the most part, homeowners to a lesser degree

Industry/Entity Type

Agriculture

Requirements
Must have
• The design must be descriptive enough to describe the effects of the product.

```html
<!DOCTYPE html>
<html lang="en">
<head>
<meta charset="utf-8">
<title>Verdant Shield – Label</title>
<link rel="stylesheet" href="https://fonts.googleapis.com/css2?family=Oswald:wght@700&family=Roboto+Condensed:wght@700&display=swap">
<style>
  :root {
    --page-bg: #ffffff;
    --frame-brown: #5a2e12;
    --frame-red: #b3271c;
    --frame-gold: #f2c230;
    --sky-top: #8fb3c9;
    --sky-low: #e8dcb0;
    --hill-brown: #4a2a10;
    --field-gold: #e2b43a;
    --lower-brown: #5b3612;
    --lower-yellow: #f7d21a;
    --ribbon-light: #fbe9a3;
    --ribbon-mid: #e9bf3c;
    --ribbon-dark: #a9741c;
    --ribbon-back: #6b3b14;
    --title-red: #c8101e;
    --copy-cream: #fff6c8;
    --brand-blue: #1b3d9a;
  }
  html, body {
    margin: 0;
    padding: 0;
    width: 1200px;
    height: 900px;
    overflow: hidden;
    background: var(--page-bg);
  }
  .canvas {
    display: block;
    width: 1200px;
    height: 900px;
  }
  .product-title {
    font-family: "Oswald", "Arial Narrow", sans-serif;
    font-weight: 700;
    font-size: 64px;
    fill: var(--title-red);
  }
  .product-claim {
    font-family: "Roboto Condensed", "Arial Narrow", sans-serif;
    font-weight: 700;
    font-size: 15px;
    fill: var(--copy-cream);
  }
  .company-name,
  .company-mark {
    font-family: "Roboto Condensed", "Arial Narrow", sans-serif;
    font-weight: 700;
    fill: var(--brand-blue);
  }
  .company-name { font-size: 17px; }
  .company-mark { font-size: 38px; }
</style>
</head>
<body>
<svg class="canvas" viewBox="0 0 1200 900" xmlns="http://www.w3.org/2000/svg">
  <defs>
    <clipPath id="label-inner">
      <ellipse cx="600" cy="470" rx="212" ry="326"/>
    </clipPath>
    <linearGradient id="sky-fill" x1="0" y1="0" x2="0" y2="1">
      <stop offset="0" stop-color="var(--sky-top)"/>
      <stop offset="1" stop-color="var(--sky-low)"/>
    </linearGradient>
    <linearGradient id="lower-fill" x1="0" y1="0" x2="0" y2="1">
      <stop offset="0" stop-color="var(--hill-brown)"/>
      <stop offset="0.45" stop-color="var(--lower-brown)"/>
      <stop offset="0.8" stop-color="#c99a1c"/>
      <stop offset="1" stop-color="var(--lower-yellow)"/>
    </linearGradient>
    <radialGradient id="dome-fill" cx="0.45" cy="0.4" r="0.6">
      <stop offset="0" stop-color="#eef3f4"/>
      <stop offset="0.55" stop-color="#c9d6da"/>
      <stop offset="0.8" stop-color="var(--field-gold)"/>
      <stop offset="1" stop-color="#a47a2a"/>
    </radialGradient>
    <linearGradient id="ribbon-fill" x1="0" y1="0" x2="0" y2="1">
      <stop offset="0" stop-color="var(--ribbon-light)"/>
      <stop offset="0.5" stop-color="var(--ribbon-mid)"/>
      <stop offset="1" stop-color="var(--ribbon-dark)"/>
    </linearGradient>
  </defs>

  <!-- Label frame -->
  <g class="label-frame">
    <ellipse cx="600" cy="470" rx="236" ry="350" fill="var(--frame-brown)"/>
    <ellipse cx="600" cy="470" rx="219" ry="333" fill="var(--frame-gold)"/>
    <ellipse cx="600" cy="470" rx="215" ry="329" fill="var(--frame-red)"/>
  </g>

  <!-- Label body -->
  <g class="label-body" clip-path="url(#label-inner)">
    <rect x="380" y="140" width="440" height="660" fill="url(#sky-fill)"/>
    <path d="M380 470 Q600 330 820 470 L820 800 L380 800 Z" fill="url(#lower-fill)"/>
    <g class="dome-illustration" role="img" aria-label="Transparent dome over a farmhouse and wheat field, with beetles and ladybugs unable to get in">
      <circle cx="600" cy="290" r="125" fill="url(#dome-fill)" opacity="0.95"/>
    </g>
  </g>

  <!-- Title ribbon -->
  <g class="title-ribbon" transform="rotate(-13 600 470)">
    <path d="M300 470 L350 440 L350 520 L300 530 L325 498 Z" fill="var(--ribbon-back)"/>
    <path d="M900 430 L850 410 L850 490 L900 490 L875 458 Z" fill="var(--ribbon-back)"/>
    <path d="M335 430 Q600 395 865 430 L865 505 Q600 470 335 505 Z" fill="url(#ribbon-fill)" stroke="var(--ribbon-dark)" stroke-width="2"/>
    <text class="product-title" x="600" y="478" text-anchor="middle">Verdant Shield</text>
  </g>

  <!-- Claim -->
  <text class="product-claim" text-anchor="end">
    <tspan x="760" y="572">100% natural</tspan>
    <tspan x="760" y="590">product that keeps</tspan>
    <tspan x="760" y="608">bugs away much longer than</tspan>
    <tspan x="760" y="626">the conventional chemicals.</tspan>
  </text>

  <!-- Company -->
  <text class="company-name" x="600" y="690" text-anchor="middle">Fieldstone Harvest Works</text>
  <text class="company-mark" x="600" y="742" text-anchor="middle">FHW</text>
</svg>
</body>
</html>
```